Farming Operation Business Card

We need a logo designed for a Farming operation. We grow walnuts, harvest walnuts, provide orchard management for customers, lease farm ground, repair farm equipment and prune trees. This is a family owned business with two boys ages 20 & 21 working under their father. I want a design and logo hip enough for the boys but not too crazy for their conservative father. Favorite colors tend to be traditional green, navy blue and grey but not all together and open to al colors.

Let me make my concept clearer - These guys are Ranchers, Cowbolys, true blue collar workers. Up at the crack of dawn, driving a tractor, preparing the earth for harvest. These men work long hours and on big equipment to produce a out of the world walnut. They get down and dirty at their job but know how to clean up and treat a woman right. Farming is their fist love, they know nothing more then digging their hands into God's earth and pouring their sweat and blood into their harvest. Please no more designs with children holding hands in the design.

Target Market(s)

Local walnut farmers

Industry/Entity Type

Farming

Contact Information for Business Card

Harlow Acres. Dale Whitcomb. 559-731-4460On back services listed: Walnut Harvesting / Orchard Management / Orchard Leasing / Equipment Repair / Pruning

Font styles to use
Serif

Requirements
Must have
• Harlow Acres
Nice to have
• A Walnut... possibly with Harlow Acres logo designed in the walnut
Should not have
• NO Squirrels / No children holing hands or pictures of people

```html
<!DOCTYPE html>
<html lang="en">
<head>
<meta charset="utf-8">
<title>Harlow Acres – Business Card</title>
<link rel="stylesheet" href="https://fonts.googleapis.com/css2?family=Open+Sans:wght@400;600;700&display=swap">
<style>
  :root {
    --backdrop: #b9b9b7;
    --card: #0b0b0b;
    --card-edge: #161616;
    --white: #f4f4f4;
    --teal: #2f6374;
    --teal-bright: #2fa3c9;
    --rule: #2a2a2a;
  }
  * { box-sizing: border-box; margin: 0; padding: 0; }
  html, body {
    width: 1200px; height: 900px; overflow: hidden;
    background: var(--backdrop);
    font-family: "Open Sans", Arial, sans-serif;
  }
  .canvas {
    position: relative; width: 1200px; height: 900px;
  }
  .card {
    position: absolute; left: 320px; width: 560px; height: 320px;
    background: radial-gradient(ellipse at 40% 35%, var(--card-edge), var(--card) 70%);
    box-shadow: 0 10px 24px rgba(0,0,0,.25);
    color: var(--white);
  }
  .card--services { top: 105px; }
  .card--contact { top: 475px; }

  /* services side */
  .brand {
    display: flex; align-items: center; justify-content: center; gap: 14px;
    margin-top: 96px;
  }
  .brand__mark { width: 30px; height: 30px; background: var(--white); }
  .brand__name {
    font-weight: 600; font-size: 34px; letter-spacing: 1.5px;
    text-transform: uppercase; color: var(--white);
  }
  .services {
    margin-top: 22px; text-align: center;
    font-weight: 600; font-size: 14px; line-height: 1.45;
  }

  /* contact side */
  .contact-brand {
    position: absolute; left: 36px; top: 38px;
    display: flex; align-items: center; gap: 16px;
  }
  .contact-brand .brand__mark { width: 44px; height: 44px; background: var(--teal-bright); opacity: .8; }
  .contact-brand .brand__name { color: var(--teal); font-size: 34px; }
  .holder {
    position: absolute; left: 36px; top: 128px;
    font-weight: 700; font-size: 17px; color: var(--teal);
  }
  .rule {
    position: absolute; height: 1px; background: var(--rule);
  }
  .rule--name { left: 190px; right: 36px; top: 142px; }
  .rule--details { left: 260px; right: 36px; top: 206px; }
  .details {
    position: absolute; right: 36px; top: 218px;
    text-align: right; font-size: 15px; line-height: 1.45;
  }
  .details__row { display: flex; justify-content: flex-end; align-items: center; gap: 8px; }
  .details__icon { width: 12px; height: 12px; flex: none; }
  .details__address { padding-right: 20px; }
</style>
</head>
<body>
<main class="canvas">

  <section class="card card--services" aria-label="Card back: services">
    <div class="brand">
      <span class="brand__mark"></span>
      <span class="brand__name">Harlow Acres</span>
    </div>
    <p class="services">
      Walnut Harvesting | Orchard Management | Orchard Leasing<br>
      Equipment Repair | Pruning
    </p>
  </section>

  <section class="card card--contact" aria-label="Card front: contact">
    <div class="contact-brand">
      <span class="brand__mark"></span>
      <span class="brand__name">Harlow Acres</span>
    </div>
    <p class="holder">Dale Whitcomb</p>
    <span class="rule rule--name"></span>
    <span class="rule rule--details"></span>
    <div class="details">
      <div class="details__row">
        <span>555-284-9173</span>
        <svg class="details__icon" viewBox="0 0 12 12" aria-hidden="true">
          <path d="M2.5 1 L4.5 1 L5.2 3.5 L4 4.5 Q5 7 7.5 8 L8.5 6.8 L11 7.5 L11 9.5 Q10.5 11 9 11 Q1 10 1 3 Q1 1.5 2.5 1 Z" fill="var(--teal)"/>
        </svg>
      </div>
      <div class="details__row">
        <span>www.website.com</span>
        <svg class="details__icon" viewBox="0 0 12 12" aria-hidden="true">
          <circle cx="6" cy="6" r="5.5" fill="var(--teal)"/>
          <path d="M0.5 6 H11.5 M6 0.5 Q3 6 6 11.5 M6 0.5 Q9 6 6 11.5" stroke="var(--card)" stroke-width="0.8" fill="none"/>
        </svg>
      </div>
      <p class="details__address">12345, Address Goes Here<br>Country Name, 123456</p>
    </div>
  </section>

</main>
</body>
</html>
```